Satchel & Compass needs new business card design

I need a new business card design. I'm looking for out-of-the-box design which represents the freedom of being a location independent entrepreneur.
I offer coaching, retreats and trips.
I would like to see designs with and without the photo.
Colors I use are black (#000000), green (#25A796) and brown (#D7C38C)
Website satchelandcompass.com

Target Market(s)

location independent entrepreneurs, digital nomads, people looking to swap the 9 to 5 for a lifestyle business

Industry/Entity Type

Business

Contact Information for Business Card

Petra Varga
Your Lifestyle Business Coach, Retreat & Trip Leader
http://satchelandcompass.com
hello@satchelandcompass.com
Live a life you don't need a holiday from

Font styles to use
Serif
Sans Serif

Requirements
Must have
• One side should contain only the logo. I would also consider having the "Live a life you don't need a holiday from" on that side too (depending on how it looks)
• Please show both sides on the designs.

```html
<!DOCTYPE html>
<html lang="en">
<head>
<meta charset="utf-8">
<title>Satchel &amp; Compass — Business Card</title>
<link rel="stylesheet" href="https://fonts.googleapis.com/css2?family=Open+Sans:ital,wght@0,400;0,600;0,700;1,400&display=swap">
<style>
  :root {
    --brand-green: #25A796;
    --brand-black: #231f20;
    --paper-white: #ffffff;
    --backdrop: #d9d9d9;
    --card-w: 720px;
    --card-h: 412px;
  }
  * { box-sizing: border-box; margin: 0; padding: 0; }
  html, body {
    width: 1105px;
    height: 1200px;
    overflow: hidden;
    background: var(--backdrop);
    font-family: "Open Sans", sans-serif;
  }
  .canvas { position: relative; width: 1105px; height: 1200px; }
  .card {
    position: absolute;
    left: 193px;
    width: var(--card-w);
    height: var(--card-h);
    overflow: hidden;
  }
  .card--front { top: 145px; background: var(--paper-white); }
  .card--back { top: 601px; background: var(--brand-green); }

  .front-shapes { position: absolute; inset: 0; }

  .brand-name {
    font-family: "Open Sans", sans-serif;
    font-weight: 700;
    text-transform: uppercase;
    letter-spacing: 1px;
    white-space: nowrap;
  }
  .front-brand {
    position: absolute;
    right: 39px;
    top: 52px;
    font-size: 34px;
    color: var(--brand-black);
  }

  .holder {
    position: absolute;
    right: 39px;
    top: 290px;
    text-align: right;
    color: var(--paper-white);
  }
  .holder__name {
    font-size: 23px;
    font-weight: 700;
    color: var(--brand-green);
    letter-spacing: 0.5px;
    line-height: 30px;
  }
  .holder__role { font-size: 19px; line-height: 26px; }

  .contact {
    position: absolute;
    left: 39px;
    top: 323px;
    list-style: none;
    color: var(--paper-white);
    font-size: 19px;
    line-height: 27px;
  }
  .contact__item { display: flex; align-items: center; gap: 10px; }
  .contact__icon { width: 18px; height: 18px; flex: none; }

  .back-pattern {
    position: absolute;
    inset: 0;
    background: linear-gradient(160deg, #2aad9c 0%, var(--brand-green) 55%, #22a190 100%);
  }
  .back-brand {
    position: absolute;
    left: 0;
    right: 0;
    top: 186px;
    text-align: center;
    font-size: 48px;
    color: var(--paper-white);
  }
  .back-tagline {
    position: absolute;
    left: 0;
    right: 0;
    top: 350px;
    text-align: center;
    font-size: 18px;
    font-style: italic;
    color: var(--paper-white);
  }
  .social {
    position: absolute;
    top: 25px;
    right: 25px;
    display: flex;
    gap: 7px;
    list-style: none;
  }
  .social__badge {
    width: 25px;
    height: 25px;
    background: var(--paper-white);
  }
</style>
</head>
<body>
<main class="canvas">

  <section class="card card--front" aria-label="Card front">
    <svg class="front-shapes" width="720" height="412" viewBox="0 0 720 412" aria-hidden="true">
      <polygon class="accent-stripe" points="0,259 362,259 348,273 0,273" fill="var(--brand-green)"/>
      <polygon class="dark-band" points="0,273 364,273 409,228 720,228 720,412 0,412" fill="var(--brand-black)"/>
    </svg>

    <div class="brand-name front-brand">Satchel &amp; Compass</div>

    <div class="holder">
      <p class="holder__name">PETRA VARGA</p>
      <p class="holder__role">Your Lifestyle Business Coach</p>
      <p class="holder__role">Retreat &amp; Trip Leader</p>
    </div>

    <ul class="contact">
      <li class="contact__item">
        <svg class="contact__icon" viewBox="0 0 18 18" aria-hidden="true">
          <rect x="1" y="4" width="16" height="11" fill="var(--brand-green)"/>
          <polyline points="1,4 9,10 17,4" fill="none" stroke="var(--brand-black)" stroke-width="1.5"/>
        </svg>
        <span>hello@satchelandcompass.com</span>
      </li>
      <li class="contact__item">
        <svg class="contact__icon" viewBox="0 0 18 18" aria-hidden="true">
          <circle cx="9" cy="9" r="8" fill="var(--brand-green)"/>
          <ellipse cx="9" cy="9" rx="3.5" ry="8" fill="none" stroke="var(--brand-black)" stroke-width="1.2"/>
          <line x1="1" y1="9" x2="17" y2="9" stroke="var(--brand-black)" stroke-width="1.2"/>
        </svg>
        <span>www.satchelandcompass.com</span>
      </li>
    </ul>
  </section>

  <section class="card card--back" aria-label="Card back">
    <div class="back-pattern" role="img" aria-label="Faint repeated brand-name pattern across the green background"></div>

    <ul class="social" aria-label="Social profiles">
      <li class="social__badge"></li>
      <li class="social__badge"></li>
      <li class="social__badge"></li>
    </ul>

    <div class="brand-name back-brand">Satchel &amp; Compass</div>
    <p class="back-tagline">Live a life you don't need a holiday from</p>
  </section>

</main>
</body>
</html>
```